Tarvel Ridge LLC

Need Professional Business cards for New Investment Fund

Target Market(s)

High Quality investors

Industry/Entity Type

Financial

Contact Information for Business Card

Phone Number +1 555 284 6193
Name Pavel Orlinsky
Title Fund Manager
email po@FundTarvel.example
Website www.FundTarvel.example

Colors

Designer to choose colors to be used in the design.

Requirements
Must have
• Must have our Logo and all of the above. Must be made so lettering and loge can be raised

```html
<!DOCTYPE html>
<html lang="en">
<head>
<meta charset="utf-8">
<title>Tarvel Ridge LLC – Business Card</title>
<link rel="stylesheet" href="https://fonts.googleapis.com/css2?family=Arimo:wght@400;700&display=swap">
<style>
  :root {
    --stage: #34373f;
    --card-front: #f5f5f5;
    --card-back: #e3e3e3;
    --green: #4caf35;
    --dark: #343d33;
    --ink: #333833;
  }
  * { box-sizing: border-box; margin: 0; padding: 0; }
  html, body {
    width: 1200px; height: 900px; overflow: hidden;
    background: var(--stage);
    font-family: "Arimo", Arial, sans-serif;
  }
  .canvas {
    position: relative; width: 1200px; height: 900px;
  }
  .card {
    position: absolute; left: 362px; width: 477px; height: 272px;
    overflow: hidden;
  }
  .card--front { top: 145px; background: var(--card-front); }
  .card--back { top: 482px; background: var(--card-back); }
  .card__name {
    position: absolute; left: 29px; top: 42px;
    font-size: 22px; font-weight: 400; color: var(--ink); letter-spacing: 0.2px;
  }
  .card__title {
    position: absolute; left: 29px; top: 73px;
    font-size: 11px; color: var(--green);
  }
  .contacts {
    position: absolute; left: 29px; top: 166px; list-style: none;
  }
  .contacts__item {
    display: flex; align-items: center; height: 16px; margin-bottom: 9px;
    font-size: 11px; color: var(--green);
  }
  .contacts__icon {
    width: 16px; height: 16px; margin-right: 11px; flex: none;
  }
  .brand {
    position: absolute; display: flex; align-items: center; gap: 7px;
  }
  .brand__mark {
    width: 14px; height: 14px; background: var(--green);
  }
  .brand__name {
    font-size: 15px; font-weight: 700; color: var(--dark); letter-spacing: 1px;
    white-space: nowrap;
  }
  .card--front .brand { left: 318px; top: 128px; }
  .card--back .brand { left: 50%; top: 128px; transform: translateX(-50%); }
  .card__band {
    position: absolute; left: 0; bottom: 0; width: 477px; height: 27px;
  }
</style>
</head>
<body>
<main class="canvas">

  <section class="card card--front" aria-label="Business card front">
    <h1 class="card__name">Pavel Orlinsky</h1>
    <p class="card__title">Fund Manager</p>

    <ul class="contacts">
      <li class="contacts__item">
        <svg class="contacts__icon" viewBox="0 0 16 16" aria-hidden="true">
          <rect width="16" height="16" rx="2" fill="var(--green)"/>
          <path d="M4 7.5c0-1.5 1.8-2.3 4-2.3s4 .8 4 2.3l-1.6.3-.3-1H5.9l-.3 1z" fill="#fff"/>
          <rect x="5" y="8.3" width="6" height="3.4" rx="0.6" fill="#fff"/>
        </svg>
        +1 555 284 6193
      </li>
      <li class="contacts__item">
        <svg class="contacts__icon" viewBox="0 0 16 16" aria-hidden="true">
          <rect width="16" height="16" rx="2" fill="var(--green)"/>
          <path d="M4 5l8 6M12 5l-8 6" stroke="#fff" stroke-width="0.9" fill="none"/>
        </svg>
        po@FundTarvel.example
      </li>
      <li class="contacts__item">
        <svg class="contacts__icon" viewBox="0 0 16 16" aria-hidden="true">
          <rect width="16" height="16" rx="2" fill="var(--green)"/>
          <circle cx="8" cy="8" r="3.8" fill="none" stroke="#fff" stroke-width="0.9"/>
          <path d="M4.2 8h7.6M8 4.2c-1.6 2.3-1.6 5.3 0 7.6M8 4.2c1.6 2.3 1.6 5.3 0 7.6" stroke="#fff" stroke-width="0.7" fill="none"/>
        </svg>
        www.FundTarvel.example
      </li>
    </ul>

    <div class="brand">
      <span class="brand__mark" aria-hidden="true"></span>
      <span class="brand__name">TARVEL RIDGE</span>
    </div>

    <svg class="card__band" viewBox="0 0 477 27" aria-hidden="true">
      <polygon points="0,5 339,5 382,27 0,27" fill="var(--dark)"/>
      <polygon points="341,0 477,0 477,27 384,27" fill="var(--green)"/>
    </svg>
  </section>

  <section class="card card--back" aria-label="Business card back">
    <div class="brand">
      <span class="brand__mark" aria-hidden="true"></span>
      <span class="brand__name">TARVEL RIDGE</span>
    </div>

    <svg class="card__band" viewBox="0 0 477 27" aria-hidden="true">
      <polygon points="0,5 339,5 382,27 0,27" fill="var(--dark)"/>
      <polygon points="341,0 477,0 477,27 384,27" fill="var(--green)"/>
    </svg>
  </section>

</main>
</body>
</html>
```